Migration and redesign of existing website to WordPress using DIVI 3

I. TASK OBJECTIVE:
- Redesign our existing website www.calderwynhealth.com.au with a fresh new look and migrate to new Wordpress site based on DIVI3 theme. The site will contain the same basic functionality as the existing site (with some small changes).

II. STYLE/ DESIGN ASPECT:
As an example of a site that I like the look of, see https://tanglorix.com/. I like the use of shadows, and this would go well with the little animations you can do with Divi (e.g. when hovering over pics).

1. What I am looking for is a design which has lots of white space, is modern and friendly looking (but still not too cute or frivolous, as we are a medical practice)
2. DESIGN that is NOT TOO rectangular or blocky.
3. Please take into consideration our Users are Older market, so any icons or navigation features need to be very easy to understand and not too small.
4. Must be easy to navigate
5. We are are happy to go with a new colour scheme, and are working on some ideas for this, but happy to take suggestions.

III. SPECIFICATIONS:
1. 5+ Pages (should flow like the current site)
2. Using Wordpress Divi 3 theme.
3. I'd like every page to have a "book now" button and a contact form in a sidebar so that users can click the button or fill in the contact form without scrolling at all. EXCEPT ON THE HOME PAGE, where there should still be a book now button (maybe on the top right in the header of all pages?), and maybe a contact us button which scrolls down to the contact area at the bottom of the HOME page. I don't think a side bar is necessarily required on the home page, but if you think it makes sense from a design perspective please let me know.
4. AT THE BOTTOM OF THE PAGE, just above the FOOTER, I'd like a row of trust logos for various organisations that we are affiliated with. (A list of this company will be provided later but you could temporarily use placeholders)

Once we have a structure in place, we can migrate most of the content. Please let me know if I'm not being clear or you need further information.

Target Market(s)

Podiatry Customers and Referrors

Industry/Entity Type

Health Care

Coding

Coded - Design and coding required

Number of Pages Required

5+ page

Colors

Designer to choose colors to be used in the design.

Requirements
Must have
• Simple to navigate.
• Contact/booking details on most if not all pages - please see specification above
• Section for Trusted Affiliates above the footer
• Wordpress using Divi3 Theme
Nice to have
• Not too busy with the design. Plenty of white space or light background.
Should not have
• Should not be complicated to navigate.
• TOO rectangular or blocky designs

```html
<!DOCTYPE html>
<html lang="en">
<head>
<meta charset="utf-8">
<title>Calderwyn Foot &amp; Ankle Clinic</title>
<link href="https://fonts.googleapis.com/css2?family=Montserrat:wght@400;600;700&family=Open+Sans:wght@400;600;700&display=swap" rel="stylesheet">
<style>
:root{
  --teal:#1a92bb;
  --teal-dark:#14779a;
  --teal-deep:#0f6282;
  --teal-light:#5fb8d6;
  --ink:#2f3338;
  --text:#5b6168;
  --muted:#8a9097;
  --pale:#eef3f5;
  --badge:#d6e3e9;
  --footer:#2b2f34;
  --footer-bottom:#222528;
  --white:#ffffff;
}
*{box-sizing:border-box;margin:0;padding:0}
html,body{width:1200px;height:4452px;overflow:hidden}
body{font-family:"Open Sans",Arial,sans-serif;color:var(--text);background:var(--white);font-size:14px;line-height:1.6}
h1,h2,h3,h4{font-family:"Montserrat",Arial,sans-serif;color:var(--ink)}
.btn{display:inline-block;padding:10px 34px;border:2px solid var(--teal);color:var(--teal);font-family:"Montserrat",sans-serif;font-weight:600;font-size:13px;border-radius:3px;background:var(--white)}
.btn--solid{background:var(--teal);color:var(--white)}
.btn--light{border-color:var(--white);color:var(--white);background:transparent}

/* top bar */
.topbar{height:40px;background:var(--teal-deep);color:var(--white);display:flex;align-items:center;padding:0 80px;font-size:13px;gap:40px}
.topbar__item{display:flex;align-items:center;gap:8px}
.topbar__social{margin-left:auto;display:flex;gap:10px}
.topbar__social span{width:14px;height:14px;border-radius:50%;background:rgba(255,255,255,.7)}

/* header */
.header{position:relative;height:120px;display:flex;align-items:center;justify-content:center;gap:14px}
.brand__mark{width:26px;height:26px;border-radius:50%;background:var(--teal)}
.brand__name{font-family:"Montserrat",sans-serif;font-weight:600;font-size:22px;color:var(--teal-dark)}
.header__book{position:absolute;right:80px;top:39px;padding:9px 26px}
.nav{height:48px;background:var(--teal);display:flex;align-items:center;padding:0 80px}
.nav a{color:var(--white);text-decoration:none;font-size:14px;padding:0 20px;height:48px;display:flex;align-items:center}
.nav a.is-active{background:var(--teal-light)}

/* hero */
.hero{position:relative;height:572px;background:linear-gradient(120deg,#c9cdd0 0%,#8c9197 40%,#5c6165 70%,#3f4346 100%);display:flex;flex-direction:column;align-items:center;justify-content:center;text-align:center;color:var(--white)}
.hero h1{color:var(--white);font-size:40px;font-weight:700;margin-top:60px}
.hero p{font-size:14px;max-width:520px;margin:6px 0 28px}
.hero .btn{margin-bottom:34px}
.hero__dots{display:flex;gap:10px}
.hero__dots span{width:10px;height:10px;border-radius:50%;background:rgba(255,255,255,.55)}
.hero__dots span:first-child{background:var(--white)}
.hero__arrow{position:absolute;top:266px;width:40px;height:40px;border-radius:50%;border:2px solid rgba(255,255,255,.8)}
.hero__arrow--prev{left:20px}.hero__arrow--next{right:20px}

/* section title */
.section-title{text-align:center;font-variant:small-caps;font-size:34px;font-weight:700;color:var(--teal-dark);letter-spacing:1px}
.section-title::after{content:"";display:block;width:60px;height:3px;background:var(--teal);margin:10px auto 0}

/* practice areas */
.practice{height:580px;padding-top:60px;background:var(--white)}
.practice__grid{display:grid;grid-template-columns:1fr 1fr;gap:50px 80px;width:800px;margin:52px auto 0}
.area__head{display:flex;align-items:center;gap:12px;margin-bottom:10px}
.area__icon{width:46px;height:46px}
.area__head h3{font-variant:small-caps;font-size:18px;color:var(--ink)}
.area p{font-size:13px;line-height:1.55}
.area .more{display:inline-block;margin-top:6px;color:var(--teal);font-weight:700;font-size:13px}

/* relief */
.relief{height:460px;background:var(--teal);display:flex;align-items:center;padding:0 120px;gap:60px}
.relief__text{width:520px;color:var(--white)}
.relief__text h2{color:var(--white);font-variant:small-caps;font-size:26px;line-height:1.2;margin-bottom:18px}
.relief__text p{font-size:13px;margin-bottom:12px}
.relief__photo{width:440px;height:350px;background:linear-gradient(135deg,#eef2f4,#c7d6dd 60%,#7fa4b6);border-radius:2px}

/* record */
.record{height:700px;display:flex;align-items:center;padding:0 120px;gap:60px}
.record__photo{width:480px;height:600px;background:linear-gradient(160deg,#d9dfe2,#b9c5cc 50%,#8fa2ab)}
.record__text{width:480px}
.record__text h2{font-variant:small-caps;font-size:26px;line-height:1.25;color:var(--teal-dark);margin-bottom:20px}
.record__text p{font-size:13px;margin-bottom:12px}
.record__text .btn{margin-top:14px}

/* team */
.team{height:628px;background:linear-gradient(180deg,var(--teal) 0%,var(--teal-dark) 100%);padding-top:52px;text-align:center}
.team .section-title{color:var(--white)}
.team .section-title::after{background:var(--white)}
.team__row{display:flex;justify-content:center;gap:40px;margin:48px 0 40px}
.member{width:190px}
.member__photo{height:260px;background:linear-gradient(180deg,#e8ecee,#c2ccd1)}
.member__name{background:var(--white);color:var(--ink);font-weight:600;padding:6px 0;font-size:15px;margin-top:6px}
.member__role{background:var(--teal-deep);color:var(--white);font-size:13px;padding:5px 0}

/* free book */
.book{height:530px;text-align:center;padding-top:38px}
.book h2{color:var(--teal);font-size:26px}
.book h3{font-size:18px;margin:8px 0 4px}
.book p{font-size:13px;color:var(--muted)}
.book__banner{display:flex;width:960px;height:250px;margin:28px auto 26px;background:var(--teal-dark);text-align:left}
.book__cover{width:380px;padding:30px 34px;color:var(--white)}
.book__cover h4{color:var(--white);font-size:30px;margin-bottom:10px}
.book__cover .author{font-size:13px;font-weight:600;margin-bottom:14px}
.book__cover .meta{font-size:11px;line-height:1.5;opacity:.85}
.book__photo{flex:1;background:linear-gradient(120deg,#5d8ca0,#2f5f73 55%,#1d4252)}

/* contact */
.contact{height:420px;background:var(--teal);padding-top:46px;text-align:center;color:var(--white)}
.contact .section-title{color:var(--white)}
.contact .section-title::after{background:var(--white)}
.contact__intro{font-size:13px;margin:18px 0 26px}
.contact__form{display:grid;grid-template-columns:300px 300px;gap:12px 24px;width:624px;margin:0 auto;text-align:left}
.field{background:var(--white);color:var(--muted);height:34px;padding:7px 12px;font-size:13px}
.field--msg{grid-column:2;grid-row:1/4;height:auto}
.contact__submit{grid-column:2;justify-self:end;width:140px;background:var(--teal-light);color:var(--white);text-align:center;padding:7px 0;font-weight:700;font-size:13px}

/* trusted affiliates */
.affiliates{height:102px;background:var(--pale);display:flex;align-items:center;justify-content:center;gap:34px}
.affiliates__label{font-family:"Montserrat",sans-serif;font-weight:600;font-size:14px;color:var(--teal-dark);margin-right:10px}
.affiliates__badge{width:130px;height:52px;border-radius:6px;background:var(--badge)}

/* footer */
.footer{height:220px;background:var(--footer);color:#b7bcc1;display:grid;grid-template-columns:260px 180px 260px 260px;gap:40px;padding:36px 80px 0;font-size:12px}
.footer h4{color:var(--white);font-size:13px;margin-bottom:12px}
.footer ul{list-style:none}
.footer li{margin-bottom:3px}
.footer li::before{content:"› ";color:var(--teal-light)}
.footer__sub{display:flex;margin-top:10px}
.footer__sub span{background:var(--white);color:var(--muted);padding:6px 10px;width:150px}
.footer__sub b{background:var(--teal);color:var(--white);padding:6px 12px}
.footer__bottom{height:32px;background:var(--footer-bottom);color:#8d9296;font-size:11px;display:flex;align-items:center;justify-content:center}
</style>
</head>
<body>

<div class="topbar">
  <div class="topbar__item">
    <svg width="14" height="14" viewBox="0 0 24 24"><path fill="#fff" d="M6.6 10.8a15 15 0 0 0 6.6 6.6l2.2-2.2a1 1 0 0 1 1-.25 11.4 11.4 0 0 0 3.6.6 1 1 0 0 1 1 1V20a1 1 0 0 1-1 1A17 17 0 0 1 3 4a1 1 0 0 1 1-1h3.5a1 1 0 0 1 1 1c0 1.25.2 2.45.6 3.6a1 1 0 0 1-.25 1z"/></svg>
    (08) 555 0142
  </div>
  <div class="topbar__item">
    <svg width="16" height="12" viewBox="0 0 16 12"><rect x="0.5" y="0.5" width="15" height="11" fill="none" stroke="#fff"/><path d="M1 1l7 5 7-5" fill="none" stroke="#fff"/></svg>
    info@calderwynhealth.com.au
  </div>
  <div class="topbar__social"><span></span><span></span><span></span><span></span><span></span></div>
</div>

<header class="header">
  <span class="brand__mark"></span>
  <span class="brand__name">Calderwyn Foot &amp; Ankle Clinic</span>
  <span class="btn btn--solid header__book">Book Now</span>
</header>

<nav class="nav">
  <a class="is-active">Home</a><a>Common Problems</a><a>Services</a><a>About</a><a>Case Histories</a><a>Helpful Information</a><a>Blog</a><a>Contact</a>
</nav>

<section class="hero">
  <div role="img" aria-label="Photo of a clinician holding a foot skeleton model" style="position:absolute;inset:0"></div>
  <h1 style="position:relative">Solutions To Common Foot Problems</h1>
  <p style="position:relative">Gentle, expert care for every step you take. Our friendly podiatrists help you move freely and live without foot pain.</p>
  <span class="btn btn--light" style="position:relative">Make An Appointment</span>
  <div class="hero__dots" style="position:relative"><span></span><span></span><span></span><span></span></div>
  <span class="hero__arrow hero__arrow--prev"></span>
  <span class="hero__arrow hero__arrow--next"></span>
</section>

<section class="practice">
  <h2 class="section-title">Practice Areas</h2>
  <div class="practice__grid">
    <article class="area">
      <div class="area__head">
        <svg class="area__icon" viewBox="0 0 46 46"><circle cx="23" cy="23" r="21" fill="none" stroke="#1a92bb" stroke-width="3"/><path d="M16 14c6 0 10 8 9 16-1 5 5 6 7 3" fill="none" stroke="#1a92bb" stroke-width="3" stroke-linecap="round"/></svg>
        <h3>Common Problem</h3>
      </div>
      <p>When you suffer from a foot or ankle problem, the pain and discomfort can make it a challenge to engage in simple, daily activities. When the pain persists, our team can help you find relief.</p>
      <span class="more">Read More ›</span>
    </article>
    <article class="area">
      <div class="area__head">
        <svg class="area__icon" viewBox="0 0 46 46"><rect x="4" y="8" width="38" height="30" rx="4" fill="none" stroke="#1a92bb" stroke-width="3"/><path d="M23 15v16M15 23h16" stroke="#1a92bb" stroke-width="3"/></svg>
        <h3>Foot &amp; Ankle Surgery</h3>
      </div>
      <p>Foot and ankle pain can be extremely distracting and uncomfortable, and some conditions may require surgery. If your foot or ankle problem requires treatment, our surgeon can guide you.</p>
      <span class="more">Read More ›</span>
    </article>
    <article class="area">
      <div class="area__head">
        <svg class="area__icon" viewBox="0 0 46 46"><circle cx="26" cy="9" r="5" fill="#1a92bb"/><path d="M8 24l14-6 8 4 8-6M22 18l-4 14-8 6M26 26l6 12" fill="none" stroke="#1a92bb" stroke-width="3" stroke-linecap="round"/></svg>
        <h3>Sport And Dance</h3>
      </div>
      <p>Special patient groups require innovative and constant care to keep their feet and legs healthy. We advise many different types of professional and amateur athletes, including runners.</p>
      <span class="more">Read More ›</span>
    </article>
    <article class="area">
      <div class="area__head">
        <svg class="area__icon" viewBox="0 0 46 46"><path d="M23 4l5 12 13 1-10 8 3 13-11-7-11 7 3-13L5 17l13-1z" fill="none" stroke="#1a92bb" stroke-width="3" stroke-linejoin="round"/></svg>
        <h3>All Our Services</h3>
      </div>
      <p>Foot, toe, or ankle pain can be stressful and can interfere with your ability to walk, stand, work, or do the activities that you enjoy. However, you may not have to live with it.</p>
      <span class="more">Read More ›</span>
    </article>
  </div>
</section>

<section class="relief">
  <div class="relief__text">
    <h2>Let Our Ashbury Vale Podiatrists Relieve Your Foot And Ankle Pain</h2>
    <p>Whether you are an office worker, pensioner, or professional athlete, nearly all people will experience problems in their feet and ankles at some point in their lives. Unfortunately, a problem in the foot can affect the whole body, causing an imbalance to spread, deformities in the foot, and pain to travel upward into the leg.</p>
    <p>It doesn't take long before a foot injury has severe wider consequences, including lost mobility, a drain on your finances, and a decline in your physical health. Over time, patients attempt to cure their conditions alone and fail, and then suffer the frustration of treating the symptoms while the cause remains.</p>
  </div>
  <div class="relief__photo" role="img" aria-label="Photo of a doctor with a stethoscope reviewing notes"></div>
</section>

<section class="record">
  <div class="record__photo" role="img" aria-label="Photo of a podiatrist examining a patient's foot"></div>
  <div class="record__text">
    <h2>A Proven Track Record Of Correcting Foot Pain In Perth Patients</h2>
    <p>At the Calderwyn Foot &amp; Ankle Clinic, we know that there are often a variety of causes of foot and ankle pain, and each must be addressed to relieve your problem for good. We examine your foot, posture, and gait to identify any biomechanical issues that could be adding to your pain, treat the problem and then help prevent it from coming back.</p>
    <p>Call the number on this page today to tell our podiatrists about your condition and schedule your appointment.</p>
    <p>Our podiatry clinic has provided comprehensive podiatric care to all age groups across the region since 1991. Since our practice was established, our success has allowed us to grow and expand our services, currently hosting six on staff podiatrists and a surgeon.</p>
    <span class="btn">Read More</span>
  </div>
</section>

<section class="team">
  <h2 class="section-title">Meet Our Team</h2>
  <div class="team__row">
    <div class="member"><div class="member__photo" role="img" aria-label="Portrait of podiatrist Hannah Brell"></div><div class="member__name">Hannah Brell</div><div class="member__role">Podiatrist</div></div>
    <div class="member"><div class="member__photo" role="img" aria-label="Portrait of podiatric surgeon Owen Tarrick"></div><div class="member__name">Owen Tarrick</div><div class="member__role">Podiatric Surgeon</div></div>
    <div class="member"><div class="member__photo" role="img" aria-label="Portrait of podiatrist Marcus Delling"></div><div class="member__name">Marcus Delling</div><div class="member__role">Podiatrist</div></div>
    <div class="member"><div class="member__photo" role="img" aria-label="Portrait of podiatrist Tessa Morrow"></div><div class="member__name">Tessa Morrow</div><div class="member__role">Podiatrist</div></div>
  </div>
  <span class="btn">Read More</span>
</section>

<section class="book">
  <h2>Free Book</h2>
  <h3>Free Foot Surgery Book by Podiatric Surgeon, Dr Owen Tarrick</h3>
  <p>This book was created to demonstrate examples of some foot conditions that can be surgically corrected by our Podiatric Surgeon, Dr Owen Tarrick.</p>
  <div class="book__banner">
    <div class="book__cover">
      <h4>Podiatric Surgery</h4>
      <div class="author">Dr Owen Tarrick, BSc, BPod, PGradDipMSc, FACPS</div>
      <div class="meta">Calderwyn Foot &amp; Ankle Clinic<br>12 Harlow Street<br>Ashbury Vale WA 6999<br>(08) 555 0142</div>
    </div>
    <div class="book__photo" role="img" aria-label="Photos of surgeons in a theatre and an operating room"></div>
  </div>
  <span class="btn">Read More</span>
</section>

<section class="contact">
  <h2 class="section-title">Contact Us</h2>
  <p class="contact__intro">Please fill out this quick contact form and someone will be in touch with you shortly</p>
  <div class="contact__form">
    <div class="field">Name*</div>
    <div class="field field--msg">Message*</div>
    <div class="field">Phone*</div>
    <div class="field">Email*</div>
    <div class="contact__submit">SUBMIT</div>
  </div>
</section>

<section class="affiliates" aria-label="Trusted affiliates">
  <span class="affiliates__label">Our Trusted Affiliates</span>
  <span class="affiliates__badge" role="img" aria-label="Affiliate badge placeholder"></span>
  <span class="affiliates__badge" role="img" aria-label="Affiliate badge placeholder"></span>
  <span class="affiliates__badge" role="img" aria-label="Affiliate badge placeholder"></span>
  <span class="affiliates__badge" role="img" aria-label="Affiliate badge placeholder"></span>
  <span class="affiliates__badge" role="img" aria-label="Affiliate badge placeholder"></span>
</section>

<footer class="footer">
  <div>
    <h4>Calderwyn Foot &amp; Ankle Clinic</h4>
    <p>We want to get to know you, and we care about our patients. Our team helps patients discover the personal and professional care of our podiatrists and staff. Have your foot and ankle treated here.</p>
  </div>
  <div>
    <h4>Quick Links</h4>
    <ul><li>Common Problems</li><li>Services</li><li>Case Histories</li><li>Information</li><li>Blog</li><li>Contact</li></ul>
  </div>
  <div>
    <h4>Office</h4>
    <ul><li>12 Harlow Street, Ashbury Vale</li><li>(08) 555 0142</li><li>(08) 555 0143</li><li>info@calderwynhealth.com.au</li><li>Mon–Sat 9:00am–5:00pm</li></ul>
  </div>
  <div>
    <h4>Subscribe</h4>
    <p>Get the latest updates and offers</p>
    <div class="footer__sub"><span>Enter Your Email</span><b>GO</b></div>
  </div>
</footer>
<div class="footer__bottom">© 2017 Calderwyn Foot &amp; Ankle Clinic. All Rights Reserved.</div>

</body>
</html>
```